Masculine Personal Stationary with custom Monogram

I need a monogram design to use both personal and for business. I would like it to be 'manly,' and it should include some sort of a cool custom monogram using my initials (DK). I need stationary and correspondence cards. I will be using a dark envelope (i'm open to color, but it needs to be a stock envelope) to mail them and I'm open to sizing, but both the cards and stationary should fit in the same sized envelope. I'm using these for both business and personal (different addresses) so I need options for the stationary...either we leave the address completely off and just do the monogram, or we do 2 versions each with a different address/contact info. I need a unique return address situation for the envelope. Either a sticker, stamp, or some other interesting option that I can apply to whatever stock envelope I buy. There is no budget for this, it needs to be very unique and feel like a present when it's opened. Die cuts, letterpress, and any other fun ideas are welcomed as long as they are able to be realistically produced. i.e. don't send something that is impossible to source or produce.

Here is a corkwall page of ideas I like:

https://www.corkwall.example/davekolt7/stationary/

I've attached an image of my current stationary set which I like, but it a little girly as well as the current monogram which I'm using but is also uninspired.

Industry/Entity Type

Business

Font styles to use
Serif
Decorative

Colors

Designer to choose colors to be used in the design.

Requirements
Must have
• a cool monogram the fits with the color theme of the design. It must be an incredible experience to open the letter. I want it to feel special, like they're receiving a gift (see nice to have). i'd like suggestions on how to package the design (i.e.. wax seal, interesting card stock textures designs, etc.). Be creative and think outside the box, the cost of the finished product isn't an issue...when opened, the recipient should say holy shit, this is the nicest, coolest letter i've ever received." Then they should want to show it to a friend. If they don't ask me where I got it from it's a fail. Help me refer you.
Nice to have
• my passion is to create great experiences for people. I own my own business and try to create great experiences for my staff and our customers. I also try to create great experiences for my family through travel and exciting/different/adventurous activities like sailing, skiing, amusement parks, zip lines, etc. I don't know if this can translate to the design...just a thought. if it does apply to the design it should be subtle.
Should not have
• gold.

```html
<!DOCTYPE html>
<html lang="en">
<head>
<meta charset="utf-8">
<title>Dorian Kell — Stationery Set</title>
<link rel="stylesheet" href="https://fonts.googleapis.com/css2?family=Libre+Caslon+Text:wght@400&family=Montserrat:wght@400;600&display=swap">
<style>
  :root{
    --backdrop:#cbb593;
    --navy:#15142f;
    --paper:#ffffff;
    --paper-soft:#f4f4f4;
    --ink:#3a3a3a;
    --shadow:0 6px 14px rgba(90,70,40,.28);
  }
  *{box-sizing:border-box;margin:0;padding:0}
  html,body{width:1200px;height:1200px;overflow:hidden}
  body{background:var(--backdrop);position:relative;font-family:"Montserrat",sans-serif}
  .piece{position:absolute;box-shadow:var(--shadow)}
  .navy{background:var(--navy);color:var(--paper)}
  .white{background:var(--paper);color:var(--ink)}

  /* brand mark: initials above the name, one font, one weight, one colour */
  .mark{
    position:absolute;
    transform:translate(-50%,-50%);
    display:flex;flex-direction:column;align-items:center;
    font-family:"Libre Caslon Text",serif;font-weight:400;
    font-size:var(--s,10px);line-height:1.05;white-space:nowrap;color:inherit;
  }
  .mark .monogram{font-size:2.2em;line-height:1;letter-spacing:.04em}
  .mark .name{margin-top:.05em}

  .panel{position:absolute;top:37px;height:293px}
  .panel-light{left:90px;width:333px;background:var(--paper);color:var(--ink)}
  .panel-dark{left:423px;width:305px;background:var(--navy);color:var(--paper)}
  .panel-stamp{left:728px;width:399px;background:linear-gradient(115deg,#b99f78 0 18%,#f3f3f3 18% 100%)}

  .lines{position:absolute;border-top:1px solid currentColor;border-bottom:1px solid currentColor;height:14px}
  .lines::after{content:"";position:absolute;left:0;right:0;top:6px;border-top:1px solid currentColor}

  .contact{position:absolute;font-size:4.6px;line-height:9px;color:var(--paper)}
  .letter p{font-size:3.6px;line-height:6px;color:#555;text-align:justify}
  .card-info{position:absolute;font-size:4.4px;line-height:8.5px;color:var(--ink)}
</style>
</head>
<body>

<!-- identity row -->
<section class="panel panel-light">
  <div class="mark" style="left:50%;top:155px;--s:29px"><span class="monogram">DK</span><span class="name">Dorian Kell</span></div>
</section>
<section class="panel panel-dark">
  <div class="mark" style="left:50%;top:155px;--s:29px"><span class="monogram">DK</span><span class="name">Dorian Kell</span></div>
</section>
<section class="panel panel-stamp" role="img" aria-label="Wooden rubber stamp pressing the Dorian Kell mark onto paper over kraft board"></section>

<!-- note cards -->
<div class="piece navy" style="left:164px;top:380px;width:202px;height:135px">
  <div class="lines" style="left:15px;top:101px;width:125px;color:#8f8fa8"></div>
  <div class="mark" style="left:169px;top:106px;--s:5px"><span class="monogram">DK</span><span class="name">Dorian Kell</span></div>
</div>
<div class="piece navy" style="left:434px;top:380px;width:260px;height:129px">
  <div class="mark" style="left:50%;top:62px;--s:7.5px"><span class="monogram">DK</span><span class="name">Dorian Kell</span></div>
</div>
<div class="piece white" style="left:731px;top:380px;width:260px;height:128px">
  <div class="mark" style="left:40px;top:92px;--s:5.5px"><span class="monogram">DK</span><span class="name">Dorian Kell</span></div>
  <div class="lines" style="left:78px;top:86px;width:162px;color:#6a6a72"></div>
</div>

<!-- envelopes -->
<div class="piece navy" style="left:165px;top:570px;width:202px;height:137px">
  <svg width="202" height="137" style="position:absolute;left:0;top:0" aria-hidden="true">
    <path d="M0 0 H202 L112 90 Q101 100 90 90 Z" fill="var(--paper-soft)"/>
  </svg>
</div>
<div class="piece navy" style="left:431px;top:582px;width:266px;height:134px">
  <div class="mark" style="left:36px;top:30px;--s:5.5px"><span class="monogram">DK</span><span class="name">Dorian Kell</span></div>
  <div style="position:absolute;left:144px;top:68px;width:98px;height:50px;border-radius:8px;background:linear-gradient(135deg,#f2f2f2,#cfcfd3)"></div>
</div>
<div class="piece" style="left:734px;top:548px;width:266px;height:170px">
  <svg width="266" height="40" style="position:absolute;left:0;top:0" aria-hidden="true">
    <path d="M0 37 L28 0 H238 L266 37 Z" fill="var(--paper-soft)"/>
  </svg>
  <div class="navy" style="position:absolute;left:0;top:37px;width:266px;height:133px">
    <div class="contact" style="left:14px;top:80px">+01-555-0142<br>info@dorian-kell.example<br>dorian-kell.example<br>48 Harbor Rd. Eastport, ME 04631</div>
    <div class="mark" style="left:229px;top:104px;--s:5.5px"><span class="monogram">DK</span><span class="name">Dorian Kell</span></div>
  </div>
</div>

<!-- folder -->
<div class="piece navy" style="left:161px;top:766px;width:285px;height:386px">
  <div class="mark" style="left:50%;top:186px;--s:11.5px"><span class="monogram">DK</span><span class="name">Dorian Kell</span></div>
</div>

<!-- letterhead -->
<div class="piece white letter" style="left:478px;top:793px;width:253px;height:342px">
  <div class="mark" style="left:60px;top:40px;--s:5px"><span class="monogram">DK</span><span class="name">Dorian Kell</span></div>
  <span style="position:absolute;right:37px;top:38px;font-size:3.8px;font-weight:600">48 Harbor Rd. Eastport, ME 04631</span>
  <div style="position:absolute;left:40px;right:37px;top:76px">
    <p>Thank you for the warm welcome last week. It was a pleasure to share an afternoon on the water with your family, and I hope the sail home was calm. I am writing to follow up on our plans for the coming season and to confirm the dates we discussed together.</p>
    <p style="margin-top:14px">Our team has prepared a short outline of the trip, including lodging, lift passes and a day at the park for the children. Please review the notes and let me know what you would change before we book anything.</p>
    <p style="margin-top:14px">I look forward to hearing from you soon and to many more adventures ahead.</p>
  </div>
  <span style="position:absolute;right:37px;top:274px;font-size:3.8px">Dorian Kell</span>
  <div style="position:absolute;right:37px;top:303px;font-size:3.6px;line-height:7px;font-weight:600;text-align:right">+01-555-0142<br>info@dorian-kell.example<br>dorian-kell.example</div>
</div>

<!-- business cards -->
<div class="piece navy" style="left:794px;top:830px;width:188px;height:102px">
  <div class="mark" style="left:50%;top:48px;--s:6.5px"><span class="monogram">DK</span><span class="name">Dorian Kell</span></div>
</div>
<div class="piece white" style="left:794px;top:976px;width:188px;height:104px">
  <div class="mark" style="left:44px;top:50px;--s:6px"><span class="monogram">DK</span><span class="name">Dorian Kell</span></div>
  <div style="position:absolute;left:93px;top:22px;height:60px;border-left:1px solid var(--ink)"></div>
  <div class="card-info" style="left:107px;top:20px"><b>Dorian Kell</b><br>Director<br><br>+01-555-0142<br>info@dorian-kell.example<br>dorian-kell.example<br>48 Harbor Rd. Eastport, ME</div>
</div>

</body>
</html>
```